Build a new Capability Statement for a labour support and maintenance company

Hi Everyone,
We wish to update our capability statement. Attached is a powerpoint that has the key ideas with random pictures we would like in the document. I have also attached a competitors document as a sample of the things we like. This document is being sent to our entire client base which includes Tier 1 mining companies like Vela Corran & KDM

Target Market(s)

Mining Companies

Industry/Entity Type

Mining

Colors

Designer to choose colors to be used in the design.

```html
<!DOCTYPE html>
<html lang="en">
<head>
<meta charset="utf-8">
<title>Karrik Capability Statement</title>
<link href="https://fonts.googleapis.com/css2?family=Russo+One&family=Rajdhani:wght@500;600;700&display=swap" rel="stylesheet">
<style>
:root{
  --bg:#c9c9c9;
  --paper:#f4f4f4;
  --ink:#1c1c1c;
  --dark:#222222;
  --orange:#f26a10;
  --amber:#fbb01a;
  --sky:#3f7fc8;
  --earth:#9a4f2a;
  --muted:#333;
}
*{box-sizing:border-box;margin:0;padding:0}
html,body{width:1200px;height:2330px;overflow:hidden;background:var(--bg)}
body{font-family:"Rajdhani",sans-serif;color:var(--ink);position:relative}
.spread{position:absolute;left:25px;top:340px;display:grid;grid-template-columns:560px 560px;grid-template-rows:792px 792px;gap:30px}
.page{position:relative;background:linear-gradient(160deg,#fbfbfb 0%,var(--paper) 55%,#e9e9e9 100%);overflow:hidden;box-shadow:0 2px 6px rgba(0,0,0,.25)}
.brand{position:absolute;display:flex;flex-direction:column;align-items:center;font-family:"Rajdhani",sans-serif;font-weight:700;color:var(--ink);line-height:1}
.brand-name{font-size:46px;letter-spacing:4px}
.brand-sub{font-size:11px;letter-spacing:3px;margin-top:3px}
.photo{position:absolute}
.photo-scene{background:linear-gradient(180deg,var(--sky) 0%,#8db6e0 45%,#c58a5c 62%,var(--earth) 100%)}
.footer-url{font-family:"Russo One",sans-serif;font-size:19px;letter-spacing:.5px;display:flex;align-items:center;gap:10px}
.footer-url svg{flex:none}
.page-bar{position:absolute;left:0;right:0;bottom:0;height:48px;background:var(--dark);color:#fff;display:flex;align-items:center;padding:0 20px 0 22px;gap:14px}
.page-bar .rule{flex:1;height:1px;background:#888}
.page-num{width:36px;height:36px;border-radius:50%;background:var(--orange);border:4px solid var(--amber);display:flex;align-items:center;justify-content:center;font-family:"Russo One",sans-serif;font-size:12px;color:#fff}
/* cover */
.cover .brand{left:0;right:0;top:28px}
.cover-title{position:absolute;left:44px;top:140px;font-family:"Russo One",sans-serif;font-weight:400;transform:skewX(-8deg)}
.cover-title .line-1{font-size:64px;color:var(--ink);letter-spacing:1px;line-height:1;padding-bottom:6px;border-bottom:2px solid var(--ink);width:480px}
.cover-title .line-2{font-size:64px;line-height:1;margin-top:6px;padding-bottom:6px;border-bottom:2px solid var(--ink);width:470px;background:linear-gradient(90deg,var(--orange),var(--amber));-webkit-background-clip:text;background-clip:text;color:transparent}
.cover-sub{position:absolute;left:46px;top:312px;font-size:20px;font-weight:600;line-height:1.25}
.cover .photo{left:40px;top:420px;width:560px;height:430px;border-radius:50% 0 0 50%/60% 0 0 40%;border-left:26px solid var(--orange)}
.cover .footer-url{position:absolute;right:26px;bottom:20px;color:#fff}
/* profile */
.profile-band{position:absolute;left:0;top:0;width:100%;height:270px;background:linear-gradient(90deg,var(--orange),var(--amber))}
.profile-title{position:absolute;left:24px;top:34px;font-family:"Russo One",sans-serif;font-weight:400;font-size:38px;line-height:1.12;color:var(--ink)}
.profile-quote{position:absolute;left:24px;top:150px;width:180px;font-size:17px;font-weight:600;line-height:1.25}
.profile .photo{left:285px;top:115px;width:275px;height:215px;border-radius:50% 0 0 50%;border-left:18px solid var(--ink)}
.profile .brand{left:28px;top:300px;align-items:flex-start}
.body-copy{position:absolute;font-size:13.4px;font-weight:500;line-height:1.52;color:var(--muted)}
.body-copy p+p{margin-top:15px}
.profile .body-copy{left:28px;top:410px;width:506px;text-align:justify}
.client-box{position:absolute;left:28px;top:642px;width:506px;padding:9px 14px;background:linear-gradient(90deg,var(--orange),#ff8a1e);border-radius:10px;color:var(--ink);font-size:17px;font-weight:700;line-height:1.25;text-align:center}
/* labour */
.labour .brand,.projects .brand{left:0;right:0;top:28px}
.labour-title{position:absolute;left:26px;top:128px;font-family:"Russo One",sans-serif;font-weight:400;font-size:32px;line-height:1.2;text-align:center;width:508px}
.labour-title .accent{background:linear-gradient(90deg,var(--orange),var(--amber));-webkit-background-clip:text;background-clip:text;color:transparent}
.labour .body-copy{left:28px;top:228px;width:506px}
.mini-photos{position:absolute;left:50px;top:378px;width:460px;display:flex;justify-content:space-between;z-index:2}
.mini-photo{width:120px;height:120px;border-radius:50%;border:14px solid var(--ink);background:linear-gradient(180deg,#9bbbd8,#b07a55)}
.labour .photo{left:28px;top:448px;width:506px;height:260px;border-radius:12px;border:2px solid var(--orange);background:linear-gradient(180deg,#b02a3a 0%,#7c2a2a 45%,#8c6a4e 75%,#4d3a2c 100%)}
/* projects */
.projects-title{position:absolute;left:28px;top:128px;font-family:"Russo One",sans-serif;font-weight:400;font-size:28px;letter-spacing:.5px}
.project-list{position:absolute;left:28px;top:176px;width:510px;font-size:11.6px;font-weight:500;line-height:1.42;color:var(--muted)}
.project{margin-bottom:13px}
.project h3{font-size:12px;font-weight:700;color:var(--orange)}
</style>
</head>
<body>
<main class="spread">

  <section class="page cover">
    <div class="brand"><span class="brand-name">KARRIK</span><span class="brand-sub">FIELD SERVICES</span></div>
    <h1 class="cover-title"><div class="line-1">CAPABILITY</div><div class="line-2">STATEMENT</div></h1>
    <p class="cover-sub">Specialists in Maintenance<br>and Earthmoving<br>Equipment</p>
    <div class="photo photo-scene" role="img" aria-label="Excavator and service utility vehicle on red earth under blue sky"></div>
    <div class="footer-url">
      <svg width="20" height="20" viewBox="0 0 20 20"><circle cx="10" cy="10" r="8" fill="none" stroke="#fbb01a" stroke-width="2"/><path d="M2 10h16M10 2c3 3 3 13 0 16M10 2c-3 3-3 13 0 16" fill="none" stroke="#fbb01a" stroke-width="1.5"/></svg>
      WWW.KARRIKFS.COM.AU
    </div>
  </section>

  <section class="page profile">
    <div class="profile-band"></div>
    <h2 class="profile-title">COMPANY<br>PROFILE</h2>
    <p class="profile-quote">We believe our repeat clients are evidence of our commitment to excellence</p>
    <div class="photo photo-scene" role="img" aria-label="Excavator beside a white service ute on site"></div>
    <div class="brand"><span class="brand-name">KARRIK</span><span class="brand-sub">FIELD SERVICES</span></div>
    <div class="body-copy">
      <p>Karrik Field Services Pty Ltd (Karrik) have a fully mobile workforce as well as an extensive schedule of plant and equipment to support any project.</p>
      <p>We are a family owned WA business backed by a loyal team of motivated and skilled individuals who are always available to meet your needs.</p>
      <p>We understand downtime can be costly to companies which is why Karrik is committed to providing cost effective and efficient solutions for your business. Project objectives are always met with outstanding client service and field excellence. Since our inception in 2011 clients who engage Karrik have become confident that they will receive professional, proficient and qualified people and plant on their jobs.</p>
    </div>
    <div class="client-box">Some past and present clients include Vela Corran, Ferrodyne, Corvel Iron, Ironbark Construction Pty Ltd, Norbay Industries, Halden Mining, Marlow Mining, Kestra Mining &amp; Kestra Civil</div>
    <footer class="page-bar">
      <div class="footer-url"><svg width="20" height="20" viewBox="0 0 20 20"><circle cx="10" cy="10" r="8" fill="none" stroke="#fbb01a" stroke-width="2"/><path d="M2 10h16M10 2c3 3 3 13 0 16M10 2c-3 3-3 13 0 16" fill="none" stroke="#fbb01a" stroke-width="1.5"/></svg>WWW.KARRIKFS.COM.AU</div>
      <span class="rule"></span><span class="page-num">01</span>
    </footer>
  </section>

  <section class="page labour">
    <div class="brand"><span class="brand-name">KARRIK</span><span class="brand-sub">FIELD SERVICES</span></div>
    <h2 class="labour-title">KARRIK LABOUR SUPPORT<br><span class="accent">&amp; RAPID RESPONSE</span></h2>
    <div class="body-copy">
      <p>Karrik is available for rapid response, onsite support and maintenance 24/7 to keep your business and equipment powering. We offer full mechanical repairs, component rebuilds and exchanges, digger support and mining vehicle specification fit outs. Karrik can source cost effective parts quality parts and OEM standards.</p>
      <p>Our dedicated team will ensure all projects are completed within specified timeframes ensuring the highest level of workmanship and safety is maintained</p>
    </div>
    <div class="mini-photos">
      <div class="mini-photo" role="img" aria-label="Service vehicles parked at a mine site"></div>
      <div class="mini-photo" role="img" aria-label="Ute in front of a large excavator"></div>
      <div class="mini-photo" role="img" aria-label="Ute beside haul equipment at a pit"></div>
    </div>
    <div class="photo" role="img" aria-label="Service ute beside large haul truck trays under a red sky"></div>
    <footer class="page-bar">
      <div class="footer-url"><svg width="20" height="20" viewBox="0 0 20 20"><circle cx="10" cy="10" r="8" fill="none" stroke="#fbb01a" stroke-width="2"/><path d="M2 10h16M10 2c3 3 3 13 0 16M10 2c-3 3-3 13 0 16" fill="none" stroke="#fbb01a" stroke-width="1.5"/></svg>WWW.KARRIKFS.COM.AU</div>
      <span class="rule"></span><span class="page-num">02</span>
    </footer>
  </section>

  <section class="page projects">
    <div class="brand"><span class="brand-name">KARRIK</span><span class="brand-sub">FIELD SERVICES</span></div>
    <h2 class="projects-title">LABOUR SUPPORT PROJECTS</h2>
    <div class="project-list">
      <div class="project"><h3>Machinery maintenance and breakdowns</h3>Load &amp; Haul / Exploration<br>12month project at Ridge C / Saltbush - commenced March 2021<br>Five full time HD Fitters on site 2:1 rotating roster<br>Value $2M</div>
      <div class="project"><h3>Underground machinery maintenance, breakdowns and rebuilds of Light Vehicles to Drill Rigs</h3>MEM maintenance / breakdowns<br>8month project at Red Hill &amp; Magpie - commenced April 2022<br>6 full time Drill Fitters, 2 Servicepeople, 2 Trades Assistants - rotating 8:6, 2:1 &amp; 3:1 rosters<br>$3.2M</div>
      <div class="project"><h3>Machinery maintenance and breakdowns</h3>Load &amp; Haul Exploration , MEM maintenance and breakdowns<br>4 Year project at Stormwell - commenced November 2020<br>4 full time Field Service Fitters in mine spec vehicles 2 HD Fitters on site and<br>2 Service people 2:1 rotating roster<br>Value $20M</div>
      <div class="project"><h3>Machinery maintenance and breakdowns</h3>Load &amp; Haul, Exploration, MEM maintenance and breakdowns<br>4 Year project at Mulga Wells - commenced January 2021<br>2 full time Field Service Fitters in mine spec vehicles , 2 HD Fitters on site and<br>2 Service people 2:1 rotating roster<br>Value $16M</div>
      <div class="project"><h3>Civil Construction - Haul road and access road construction</h3>MEM maintenance and breakdowns<br>13 month project at Harlow Peak - commencing January 2020<br>6 full time Field Service Fitters in mine spec vehicles and 2 Service<br>person 2:1 &amp; 3:1 roster<br>Value $2.5M</div>
    </div>
    <footer class="page-bar">
      <div class="footer-url"><svg width="20" height="20" viewBox="0 0 20 20"><circle cx="10" cy="10" r="8" fill="none" stroke="#fbb01a" stroke-width="2"/><path d="M2 10h16M10 2c3 3 3 13 0 16M10 2c-3 3-3 13 0 16" fill="none" stroke="#fbb01a" stroke-width="1.5"/></svg>WWW.KARRIKFS.COM.AU</div>
      <span class="rule"></span><span class="page-num">03</span>
    </footer>
  </section>

</main>
</body>
</html>
```